Social Media Graphics - Copperfield Loop

Create 6-7 individual social media graphics (square size) to encourage folks to join our online course, using either of the text below (only one set of text per graphic:

The Lantern Ridge Method
How to Create a 7-Figure Business From Scratch
Sign Up Today!

Or

The Lantern Ridge Method
Fast-track Your Way to a Multi-Million Business!
Sign Up Today!

For the color scheme of the graphics, use 1 or 2 colors in the color palette attached; or use any colors that look nice with their outfits; AVOID using red, white and blue altogether because it will look like an Independence Day (4th of July) graphic and we don’t want that; make sure the graphics appeal to both men and women

Make sure each graphic contains 1 of the 2 pics attached; and make sure one of the graphics is all TEXT only.

Target Market(s)

men and women looking to make more money

Industry/Entity Type

entrepreneurship

Requirements
Must have
• see the text document attached
Nice to have
• We are open to a nice color design; the color palette colors are not required, especially we don't want red, white and blue used together
Should not have
• AVOID using red, white and blue altogether because it will look like an Independence Day (4th of July) graphic and we dont want that

```html
<!DOCTYPE html>
<html lang="en">
<head>
<meta charset="utf-8">
<title>The Lantern Ridge Method – Sign Up Today</title>
<link rel="stylesheet" href="https://fonts.googleapis.com/css2?family=Archivo+Black&family=Oswald:wght@600;700&display=swap">
<style>
  :root {
    --night: #0d1426;
    --dusk: #1c2140;
    --ember: #c4451e;
    --flare: #f08a2c;
    --gold-light: #fff4cf;
    --gold: #e9c77b;
    --gold-deep: #a87a2c;
    --cream: #fffaf0;
    --maroon: #3a0d10;
  }
  * { margin: 0; padding: 0; box-sizing: border-box; }
  html, body { width: 1200px; height: 1200px; overflow: hidden; background: var(--night); }
  .poster { position: relative; width: 1200px; height: 1200px; overflow: hidden; }

  .city-backdrop {
    position: absolute; inset: 0;
    background:
      radial-gradient(ellipse 45% 30% at 88% 42%, rgba(240,138,44,.75), transparent 70%),
      radial-gradient(ellipse 40% 25% at 60% 10%, rgba(233,199,123,.25), transparent 70%),
      radial-gradient(ellipse 35% 30% at 95% 10%, rgba(40,90,200,.55), transparent 70%),
      linear-gradient(180deg, var(--dusk) 0%, #2a1f38 40%, #3a1d22 60%, var(--night) 100%);
  }

  .hosts-photo {
    position: absolute; left: 330px; top: 320px; width: 750px; height: 740px;
    background:
      radial-gradient(ellipse 28% 40% at 28% 45%, rgba(150,40,50,.85), transparent 75%),
      radial-gradient(ellipse 28% 40% at 75% 40%, rgba(60,40,35,.9), transparent 75%),
      radial-gradient(ellipse 50% 50% at 50% 50%, rgba(30,20,25,.6), transparent 80%);
  }

  .title-frame { position: absolute; left: 44px; top: 56px; width: 364px; height: 300px; }
  .title-frame svg { position: absolute; inset: 0; }
  .title-word {
    position: absolute; left: 0; width: 100%; text-align: center;
    font-family: "Archivo Black", sans-serif; line-height: 1;
    color: var(--cream);
  }
  .title-the { top: -28px; font-size: 72px; }
  .title-lantern {
    top: 102px; font-size: 54px; letter-spacing: -1px;
    transform: scaleY(2); transform-origin: center top;
    background: linear-gradient(180deg, var(--gold-light) 0%, var(--gold) 55%, var(--gold-deep) 100%);
    -webkit-background-clip: text; background-clip: text; color: transparent;
  }
  .title-ridge { top: 262px; font-size: 78px; }

  .title-method {
    position: absolute; left: 448px; top: 78px;
    font-family: "Oswald", sans-serif; font-weight: 600; font-size: 218px; line-height: 1;
    letter-spacing: 4px;
    background: linear-gradient(180deg, var(--cream) 0%, var(--gold-light) 40%, var(--gold) 75%, var(--gold-deep) 100%);
    -webkit-background-clip: text; background-clip: text; color: transparent;
  }

  .gold-swoosh { position: absolute; left: 0; top: 880px; width: 1200px; height: 320px; }

  .headline {
    position: absolute; left: 0; top: 770px; width: 1200px; text-align: center;
    font-family: "Archivo Black", sans-serif; font-size: 72px; line-height: 90px;
    text-shadow: 0 3px 8px rgba(0,0,0,.7);
  }
  .headline .line-light { color: var(--cream); display: block; }
  .headline .line-gold { color: var(--gold); display: block; }

  .cta {
    position: absolute; left: 192px; top: 1062px; width: 804px; height: 96px;
    border-radius: 48px;
    background: linear-gradient(180deg, var(--cream) 0%, var(--gold-light) 45%, var(--gold) 100%);
    display: flex; align-items: center; justify-content: center;
    font-family: "Archivo Black", sans-serif; font-size: 70px; color: var(--maroon);
    box-shadow: 0 0 30px rgba(240,170,80,.4);
  }
</style>
</head>
<body>
<main class="poster">
  <div class="city-backdrop" role="img" aria-label="Night city skyline under a dusky sky with a glowing orange sunset and golden bokeh lights"></div>
  <div class="hosts-photo" role="img" aria-label="Photo of the two course hosts smiling, a woman in a red top and a man in a black jacket"></div>

  <div class="title-frame">
    <svg viewBox="0 0 364 300" width="364" height="300" aria-hidden="true">
      <g stroke="#e9c77b" stroke-width="4" fill="none">
        <polyline points="70,2 2,2 2,298 46,298"/>
        <polyline points="294,2 362,2 362,298 318,298"/>
      </g>
    </svg>
    <div class="title-word title-the">THE</div>
    <div class="title-word title-lantern">LANTERN</div>
    <div class="title-word title-ridge">RIDGE</div>
  </div>
  <h1 class="title-method">METHOD</h1>

  <svg class="gold-swoosh" viewBox="0 0 1200 320" aria-hidden="true">
    <defs>
      <linearGradient id="swooshGold" x1="0" x2="1">
        <stop offset="0" stop-color="#a87a2c"/>
        <stop offset=".5" stop-color="#fff4cf"/>
        <stop offset="1" stop-color="#a87a2c"/>
      </linearGradient>
    </defs>
    <path d="M0 120 Q600 330 1200 0" stroke="url(#swooshGold)" stroke-width="5" fill="none"/>
    <path d="M0 175 Q600 345 1200 60" stroke="url(#swooshGold)" stroke-width="3" fill="none" opacity=".7"/>
  </svg>

  <p class="headline">
    <span class="line-light">FAST-TRACK YOUR WAY</span>
    <span class="line-gold">TO A MULTI-MILLION</span>
    <span class="line-light">BUSINESS!</span>
  </p>

  <div class="cta">SIGN UP TODAY!</div>
</main>
</body>
</html>
```